VELMARO CREST ADVISORY

Need a Boucher designed with vibrant colours and well aligned. The content is there in the word file what I have attached. The heading and the subject of each paragraph has to be separated by designing accordingly. I would appreciate if nice hd pictures of stock market/trading/forex/consulting can be accommodated with this.

Target Market(s)

traders, stock traders, business entrepreneurs

Font styles to use
Sans Serif

Requirements
Must have
• Images from stock market and charts
Nice to have
• I want it to look elegant as this goes to the trading community.
Should not have
• Don't want anything that looks goody or fashionable since its a professional broucher.

```html
<!DOCTYPE html>
<html lang="en">
<head>
<meta charset="utf-8">
<title>Velmaro Crest Advisory – Trading Brochure</title>
<link href="https://fonts.googleapis.com/css2?family=Montserrat:wght@400;500;600;700;800&display=swap" rel="stylesheet">
<style>
:root{
  --navy:#14203f;
  --blue:#1f5bd6;
  --blue-deep:#163fa8;
  --sky:#5fa8f0;
  --orange:#f7931e;
  --orange-deep:#e8741a;
  --ink:#3a3f4b;
  --muted:#7b8190;
  --paper:#ffffff;
  --bg:#e9ebef;
  --photo-a:#c9ccd2;
  --photo-b:#8e939c;
}
*{margin:0;padding:0;box-sizing:border-box}
html,body{width:1200px;height:2768px;overflow:hidden;background:var(--bg);font-family:"Montserrat",sans-serif;color:var(--ink)}
.canvas{position:relative;width:1200px;height:2768px}
.page{position:absolute;width:540px;height:763px;background:var(--paper);overflow:hidden;box-shadow:0 6px 18px rgba(20,32,63,.12)}
.page--hero{left:220px;top:40px;transform:scale(1.4074);transform-origin:0 0}
.page--a{left:40px;top:1150px}
.page--b{left:620px;top:1150px}
.page--c{left:40px;top:1953px}
.page--d{left:620px;top:1953px;background:var(--blue)}
.abs{position:absolute}
.brand{display:flex;align-items:center;gap:7px;font-weight:800;font-size:15px;letter-spacing:1px;color:var(--navy)}
.brand__dot{width:12px;height:12px;background:var(--orange)}
.brand--light{color:#fff}
.year-tab{right:20px;top:0;width:48px;height:68px;background:var(--blue);color:#fff;font-size:8px;font-weight:600;display:flex;align-items:flex-end;justify-content:center;padding-bottom:8px}
.cover__title{left:36px;top:150px;width:300px;font-weight:800;font-size:27px;line-height:1.12;color:var(--navy);text-transform:uppercase}
.cover__title em{font-style:normal;color:var(--orange)}
.cover__byline{left:36px;top:440px;font-size:10px;line-height:1.5;color:var(--ink);font-weight:500}
.cover__photo{right:0;top:110px;width:300px;height:470px;background:linear-gradient(160deg,var(--photo-a),var(--photo-b))}
.shapes{left:0;bottom:0;width:540px;height:260px}
.page-head{left:30px;top:28px;right:30px;display:flex;justify-content:space-between;align-items:center}
.page-head h2{font-size:15px;font-weight:700;color:var(--navy)}
.page-head h2 em{font-style:normal;color:var(--blue)}
.page-head .brand{font-size:12px}
.page-head .brand__dot{width:9px;height:9px}
.body-text{font-size:7.4px;line-height:1.6;color:var(--ink)}
.body-text p{margin-bottom:8px}
.body-text strong{color:var(--navy);font-weight:700}
.photo-strip{background:linear-gradient(120deg,#2b3547,#566173)}
.points li{list-style:none;display:flex;gap:10px;align-items:flex-start;margin-bottom:14px}
.points__icon{flex:0 0 22px;height:22px;border-radius:50%;background:var(--orange);display:flex;align-items:center;justify-content:center}
.points strong{color:var(--navy)}
.footer{left:0;bottom:0;width:540px;height:40px;display:flex;align-items:center;padding-left:30px;font-size:8px;font-weight:600;color:var(--blue);letter-spacing:.5px}
.footer__bar{position:absolute;right:0;bottom:0;width:180px;height:12px;background:var(--blue)}
.footer__bar::before{content:"";position:absolute;left:-60px;top:0;width:60px;height:12px;background:var(--orange)}
.contact__square{right:30px;top:0;width:60px;height:80px;background:var(--orange)}
.contact__title{left:40px;top:90px;font-size:24px;font-weight:800;color:var(--orange);letter-spacing:1px}
.contact__block{left:40px;width:300px;color:#fff;font-size:9px;line-height:1.55}
.contact__block h3{font-size:9.5px;font-weight:700;margin-bottom:2px}
.contact__brand{left:40px;bottom:60px}
</style>
</head>
<body>
<div class="canvas">

  <!-- Cover (large) -->
  <section class="page page--hero">
    <div class="abs brand" style="left:36px;top:44px"><span class="brand__dot"></span>VELMARO</div>
    <div class="abs year-tab">2020</div>
    <div class="abs cover__photo" role="img" aria-label="City skyline with stock market chart overlay"></div>
    <h1 class="abs cover__title"><em>“Trading”</em> a serious business, importance of capital and the rise in proprietary trading firm</h1>
    <p class="abs cover__byline">By Velmaro Crest Advisory<br>Daren Holloway</p>
    <svg class="abs shapes" viewBox="0 0 540 260" aria-hidden="true">
      <polygon points="0,120 150,40 150,260 0,260" fill="#f2f4f8"/>
      <polygon points="0,150 120,90 120,260 0,260" fill="var(--orange)"/>
      <polygon points="60,260 200,120 260,260" fill="var(--blue)"/>
      <polygon points="150,260 320,60 360,260" fill="var(--sky)" opacity=".85"/>
      <polygon points="300,260 460,30 540,30 540,260" fill="var(--blue-deep)"/>
      <polygon points="420,260 540,110 540,260" fill="var(--orange)"/>
    </svg>
  </section>

  <!-- Cover (spread) -->
  <section class="page page--a">
    <div class="abs brand" style="left:36px;top:44px"><span class="brand__dot"></span>VELMARO</div>
    <div class="abs year-tab">2020</div>
    <div class="abs cover__photo" role="img" aria-label="City skyline with stock market chart overlay"></div>
    <h1 class="abs cover__title"><em>“Trading”</em> a serious business, importance of capital and the rise in proprietary trading firm</h1>
    <p class="abs cover__byline">By Velmaro Crest Advisory<br>Daren Holloway</p>
    <svg class="abs shapes" viewBox="0 0 540 260" aria-hidden="true">
      <polygon points="0,120 150,40 150,260 0,260" fill="#f2f4f8"/>
      <polygon points="0,150 120,90 120,260 0,260" fill="var(--orange)"/>
      <polygon points="60,260 200,120 260,260" fill="var(--blue)"/>
      <polygon points="150,260 320,60 360,260" fill="var(--sky)" opacity=".85"/>
      <polygon points="300,260 460,30 540,30 540,260" fill="var(--blue-deep)"/>
      <polygon points="420,260 540,110 540,260" fill="var(--orange)"/>
    </svg>
  </section>

  <!-- Inside page 1 -->
  <section class="page page--b">
    <header class="abs page-head">
      <h2><em>Trading</em> is a serious business</h2>
      <div class="brand"><span class="brand__dot"></span>VELMARO</div>
    </header>
    <div class="abs body-text" style="left:30px;top:70px;width:480px">
      <p>Over the last decade, markets have rewarded those who treat trading as a discipline rather than a pastime. Capital, process and risk control separate a lasting desk from a short run of luck. This paper sets out why structure matters and how professional firms apply it every single day.</p>
      <p>Proprietary trading firms provide capital, tools and oversight to skilled traders. In return, traders share profits and follow firm rules on exposure, drawdown and position size. The model has grown quickly as technology lowers costs and opens access to global venues.</p>
    </div>
    <div class="abs photo-strip" style="left:30px;top:200px;width:480px;height:150px" role="img" aria-label="Trading screens with market charts"></div>
    <ul class="abs points body-text" style="left:30px;top:380px;width:480px">
      <li><span class="points__icon"><svg width="10" height="10" viewBox="0 0 10 10"><path d="M1 5l3 3 5-6" stroke="#fff" stroke-width="1.6" fill="none"/></svg></span><span><strong>SINGLE TRADING RULE –</strong> Define entry, exit and size before any order is placed, and keep the same rule through winning and losing weeks.</span></li>
      <li><span class="points__icon"><svg width="10" height="10" viewBox="0 0 10 10"><path d="M1 5l3 3 5-6" stroke="#fff" stroke-width="1.6" fill="none"/></svg></span><span><strong>CAPITAL PROTECTION –</strong> Cap daily loss and total drawdown so one poor session never removes the ability to trade tomorrow.</span></li>
      <li><span class="points__icon"><svg width="10" height="10" viewBox="0 0 10 10"><path d="M1 5l3 3 5-6" stroke="#fff" stroke-width="1.6" fill="none"/></svg></span><span><strong>PATIENCE AND REVIEW –</strong> Log every trade, review results weekly and refine the plan only when the data supports a change.</span></li>
    </ul>
    <footer class="abs footer">WWW.VELMAROCREST.COM<span class="footer__bar"></span></footer>
  </section>

  <!-- Inside page 2 -->
  <section class="page page--c">
    <header class="abs page-head">
      <h2><em>Trading</em> is a serious business</h2>
      <div class="brand"><span class="brand__dot"></span>VELMARO</div>
    </header>
    <div class="abs body-text" style="left:30px;top:70px;width:480px">
      <p><strong>ABOUT CAPITAL –</strong> A trader with limited funds is forced to take larger risks to reach meaningful returns. Adequate capital lets risk per trade stay small while results still compound over time.</p>
      <p>Trading on money without an edge rarely ends well. Firms that pair capital with training and clear limits give traders the space to build a stable, measured record.</p>
    </div>
    <div class="abs photo-strip" style="left:30px;top:190px;width:230px;height:200px" role="img" aria-label="Business team meeting in a consulting office"></div>
    <div class="abs body-text" style="left:280px;top:190px;width:230px">
      <p>A funded desk also brings shared research, faster execution and peers who challenge each idea. These benefits are hard to recreate alone and explain the steady rise of proprietary firms across major markets.</p>
    </div>
    <div class="abs body-text" style="left:30px;top:410px;width:480px">
      <p>For the serious trader, the question is no longer whether to join a firm but which firm offers the right mix of capital, support and fair terms. Choose carefully and treat the decision as a business choice.</p>
    </div>
    <footer class="abs footer">WWW.VELMAROCREST.COM<span class="footer__bar"></span></footer>
  </section>

  <!-- Back cover -->
  <section class="page page--d">
    <div class="abs contact__square"></div>
    <h2 class="abs contact__title">CONTACT US</h2>
    <div class="abs contact__block" style="top:140px">
      <h3>International Office Address</h3>
      <p>Velmaro Asset Management Pte Ltd<br>14 Harbourline Road, #05-02<br>Singapore 000000<br>Phone No.: +65 0000 1234</p>
    </div>
    <div class="abs contact__block" style="top:240px">
      <h3>Address</h3>
      <p>Velmaro Crest Advisory<br>22 Lakeview Terrace, Block B, Ridge Road<br>Bengaluru 000000, India<br>Phone No.: +91 00 0000 0000</p>
    </div>
    <div class="abs contact__block" style="top:340px">
      <h3>WhatsApp No.</h3>
      <p>+91 00000 00000</p>
    </div>
    <svg class="abs" style="right:0;bottom:0" width="260" height="200" viewBox="0 0 260 200" aria-hidden="true">
      <polygon points="260,20 260,200 100,200" fill="var(--orange)"/>
      <polygon points="260,110 260,200 180,200" fill="#ffffff"/>
    </svg>
    <div class="abs brand brand--light contact__brand"><span class="brand__dot"></span>VELMARO</div>
  </section>

</div>
</body>
</html>
```